Jewelry Back Card Graphic Design

I am looking for a graphic design to print out and put in the back of the jewelry box for my long-distance jewelry. I attached an example that I am now using for the "still harbor jewelry" so you can see what it's used for.

But this card needs to relate to people who are in a long-distance relationship or friendship, so it needs to resonate with them when they see it on the website and open the box if they receive the jewelry as a gift.

I attached a rough idea that I sketched myself, but you can be creative and create anything else if you have a better idea.

It needs to be square.

Looking forward to the results!

```html
<!DOCTYPE html>
<html lang="en">
<head>
<meta charset="UTF-8">
<title>A True Connection Goes Beyond Horizons</title>
<link rel="stylesheet" href="https://fonts.googleapis.com/css2?family=Courier+Prime&display=swap">
<style>
  :root {
    --sky-top: #3a5185;
    --sky-dusk: #8d89b6;
    --sky-blush: #dcbcd6;
    --sky-pink: #f1c7d9;
    --horizon-glow: #f8c3c8;
    --sea-coral: #f6b6b8;
    --sea-lilac: #c3b8d6;
    --sea-bottom: #84a9d9;
    --ink-light: #ffffff;
  }
  html, body {
    margin: 0;
    padding: 0;
    width: 1200px;
    height: 1200px;
    overflow: hidden;
  }
  .card {
    position: relative;
    width: 1200px;
    height: 1200px;
    overflow: hidden;
    background: linear-gradient(
      to bottom,
      var(--sky-top) 0%,
      #4a6198 11%,
      var(--sky-dusk) 24%,
      var(--sky-blush) 35%,
      var(--sky-pink) 46%,
      #f3c2d2 54%,
      var(--sea-coral) 63%,
      #e9b6c0 70%,
      var(--sea-lilac) 80%,
      #a1b3de 90%,
      var(--sea-bottom) 100%
    );
  }
  .horizon-band {
    position: absolute;
    left: 0;
    top: 651px;
    width: 1200px;
    height: 90px;
    background: linear-gradient(to bottom, rgba(255, 220, 224, 0.45), rgba(255, 220, 224, 0));
    border-top: 1px solid rgba(255, 230, 232, 0.35);
  }
  .motto-arc {
    position: absolute;
    inset: 0;
  }
  .motto-text {
    font-family: "Courier Prime", "Courier New", monospace;
    font-size: 30px;
    fill: var(--ink-light);
    letter-spacing: 2px;
  }
</style>
</head>
<body>
  <main class="card">
    <div class="horizon-band"></div>
    <svg class="motto-arc" width="1200" height="1200" viewBox="0 0 1200 1200" aria-labelledby="motto">
      <defs>
        <linearGradient id="arc-fade" gradientUnits="userSpaceOnUse" x1="0" y1="254" x2="0" y2="716">
          <stop offset="0" stop-color="#ffffff" stop-opacity="1"/>
          <stop offset="0.55" stop-color="#ffffff" stop-opacity="0.75"/>
          <stop offset="1" stop-color="#ffffff" stop-opacity="0.25"/>
        </linearGradient>
        <path id="motto-path" d="M 236 607 A 364 364 0 0 1 964 607"/>
      </defs>
      <path class="horizon-ring" d="M 264 716 A 353 353 0 1 1 936 716" fill="none" stroke="url(#arc-fade)" stroke-width="4" stroke-linecap="round"/>
      <text id="motto" class="motto-text">
        <textPath href="#motto-path" textLength="1140" lengthAdjust="spacing">A TRUE CONNECTION GOES BEYOND HORIZONS</textPath>
      </text>
    </svg>
  </main>
</body>
</html>
```